Business Card Design Needed

Business car design required, logo will be supplied.

Brackenfield Heat Surveyors are looking to become the leading provider of energy performance certificates to estate agents, landlords and home owners in the Yorkshire region of the UK.

The business card must be double sided and professional looking. Estate agents receive hundreds of cards from contractors and our card must stand out.

I require a two sided business card that is clean, modern and created by a designer that can think outside of the box.

Brand colours can be supplied .

Please ask if you have any questions.

Target Market(s)

Estate agents, landlords and property owners

Industry/Entity Type

Property - estate agency - energy consultants

Contact Information for Business Card

Tomas Birchwell - Energy Assessor - 07351642170 - www.BrackenfieldHSV.co.uk - info@brackenfieldhsv.co.uk

Font styles to use
Serif
Sans Serif

Colors
00AB8E
00BBA5
67D7C9
C6EFE9
E9F9F6

Requirements
Must have
• Use the provided logo, clean, professional and stand out from the crowd
Nice to have
• Clever use of text, spacing and brand colours
Should not have
• Clip art

```html
<!DOCTYPE html>
<html lang="en">
<head>
<meta charset="utf-8">
<title>Brackenfield Heat Surveyors – Business Card</title>
<link rel="stylesheet" href="https://fonts.googleapis.com/css2?family=Questrial&display=swap">
<style>
  :root {
    --bg: #d2d2d2;
    --card: #1c1c1c;
    --edge: #c8dc14;
    --blue: #0a6fb0;
    --lime: #c8dc1e;
    --white: #f2f2f2;
    --deboss: #383838;
  }
  * { margin: 0; padding: 0; box-sizing: border-box; }
  html, body {
    width: 1200px; height: 800px; overflow: hidden;
    background: var(--bg);
    font-family: "Questrial", "Helvetica Neue", Arial, sans-serif;
  }
  .canvas {
    width: 1200px; height: 800px;
    display: flex; flex-direction: column; align-items: center; justify-content: center;
    gap: 40px;
  }
  .card {
    position: relative;
    width: 560px; height: 320px;
    background: var(--card);
    border-left: 2px solid var(--edge);
    border-bottom: 2px solid var(--edge);
    overflow: hidden;
  }
  /* brand lockup */
  .brand {
    position: absolute; left: 0; right: 0; top: 62px;
    display: flex; align-items: center; justify-content: center; gap: 14px;
    white-space: nowrap;
  }
  .brand-dot {
    width: 30px; height: 30px; border-radius: 50%;
    background: var(--blue); flex: none;
  }
  .brand-divider { width: 1px; height: 40px; background: var(--blue); flex: none; }
  .brand-name {
    color: var(--blue); font-size: 22px; letter-spacing: 1.5px; text-transform: uppercase;
  }
  /* front */
  .person { position: absolute; left: 40px; top: 158px; }
  .person-name { color: var(--blue); font-size: 22px; text-transform: uppercase; line-height: 1; }
  .person-role { color: var(--lime); font-size: 14px; text-transform: uppercase; margin-top: 6px; }
  .rule {
    position: absolute; left: 40px; right: 40px; top: 210px;
    height: 1px; background: var(--blue);
  }
  .contacts {
    position: absolute; left: 40px; top: 226px;
    list-style: none; color: var(--white); font-size: 16px;
  }
  .contacts li { display: flex; align-items: center; gap: 8px; line-height: 1.55; }
  .contacts svg { width: 13px; height: 13px; fill: var(--blue); flex: none; }
  .website {
    position: absolute; right: 40px; top: 229px;
    color: var(--white); font-size: 15px;
  }
  /* back */
  .back .brand { top: 50%; transform: translateY(-50%); gap: 16px; }
  .back .brand-dot { width: 38px; height: 38px; background: none; border: 3px solid var(--deboss); }
  .back .brand-divider { height: 50px; background: var(--deboss); }
  .back .brand-name { color: var(--deboss); font-size: 24px; }
</style>
</head>
<body>
<main class="canvas">
  <section class="card front" aria-label="Card front">
    <div class="brand">
      <span class="brand-dot"></span>
      <span class="brand-divider"></span>
      <span class="brand-name">Brackenfield Heat Surveyors</span>
    </div>
    <div class="person">
      <p class="person-name">Tomas Birchwell</p>
      <p class="person-role">Energy Assessor</p>
    </div>
    <div class="rule"></div>
    <ul class="contacts">
      <li>
        <svg viewBox="0 0 24 24" aria-hidden="true"><path d="M6.6 10.8a15.1 15.1 0 0 0 6.6 6.6l2.2-2.2c.3-.3.7-.4 1-.2 1.1.4 2.3.6 3.6.6.6 0 1 .4 1 1V20c0 .6-.4 1-1 1A17 17 0 0 1 3 4c0-.6.4-1 1-1h3.5c.6 0 1 .4 1 1 0 1.2.2 2.4.6 3.6.1.3 0 .7-.2 1z"/></svg>
        07351642170
      </li>
      <li>
        <svg viewBox="0 0 24 24" aria-hidden="true"><path d="M2 5h20v14H2z M2 5l10 8 10-8"/></svg>
        info@brackenfieldhsv.co.uk
      </li>
    </ul>
    <p class="website">www.BrackenfieldHSV.co.uk</p>
  </section>

  <section class="card back" aria-label="Card back">
    <div class="brand">
      <span class="brand-dot"></span>
      <span class="brand-divider"></span>
      <span class="brand-name">Brackenfield Heat Surveyors</span>
    </div>
  </section>
</main>
</body>
</html>
```